Stationery Design Project for Lakemont Kenbu Kai Karate Studio

We Need a Stationery Design for a Karate School Teaching Okinawa Shorin Ryu Karate in Harlow Springs, Ohio, U.S.A.

Target Market(s)

Adults Base Western Speaking aged between 25 and 65 yrs, old that handle household budgets

Industry/Entity Type

School

Requirements
Must have
• Name of business: Lakemont Kenbu Kai Karate Studio
Address: Maplecrest Plaza 38214 US Hwy. 61
Harlow Springs, Ohio. 33812
Phone # : 407-555-0183
email : Lakemontkenbukaistudio@samplemail.net
Logo - attatched

```html
<!DOCTYPE html>
<html lang="en">
<head>
<meta charset="utf-8">
<title>Lakemont Kenbu Kai Karate Studio – Business Card</title>
<link href="https://fonts.googleapis.com/css2?family=Lato:wght@400;700;900&display=swap" rel="stylesheet">
<style>
  :root {
    --bg: #e6e6e6;
    --card-white: #ffffff;
    --card-grey: #f1f1f1;
    --red: #d0112b;
    --red-deep: #a80c22;
    --gold: #e8b54a;
    --ink: #1e1e1e;
    --ink-soft: #3a3a3a;
    --faint: rgba(0,0,0,0.045);
    --faint-red: rgba(90,0,10,0.16);
  }
  * { box-sizing: border-box; margin: 0; padding: 0; }
  html, body {
    width: 1200px; height: 901px; overflow: hidden;
    background: var(--bg);
    font-family: "Lato", Arial, sans-serif;
  }
  .sheet {
    position: relative; width: 1200px; height: 901px;
    display: flex; align-items: center; justify-content: center; gap: 40px;
  }
  .card {
    position: relative; width: 540px; height: 309px; overflow: hidden;
    box-shadow: 0 6px 18px rgba(0,0,0,0.18);
  }
  /* Front */
  .card--front {
    background: linear-gradient(90deg, var(--card-white) 0%, var(--card-white) 55%, var(--card-grey) 100%);
  }
  .card--front .decor-circle {
    position: absolute; width: 300px; height: 300px; border-radius: 50%;
    right: -50px; top: -10px; background: var(--faint);
  }
  .contact {
    position: absolute; left: 36px; top: 62px; color: var(--ink-soft);
    font-size: 13px; line-height: 1.35;
  }
  .contact .person { color: var(--red); font-size: 16px; text-transform: uppercase; letter-spacing: 0.3px; }
  .contact .role { font-size: 11px; color: var(--ink); margin-bottom: 16px; }
  .contact .studio { color: var(--red); font-size: 13.5px; text-transform: uppercase; letter-spacing: 0.3px; }
  .contact .address { margin-bottom: 16px; }
  .contact .label { color: var(--red); margin-right: 5px; }
  .brand {
    position: absolute; right: 30px; top: 66px; width: 190px;
    display: flex; flex-direction: column; align-items: center; gap: 14px;
  }
  .brand .mark-dot {
    width: 58px; height: 58px; border-radius: 50%; background: var(--red);
  }
  .brand .name {
    font-weight: 900; font-size: 24px; line-height: 1.05; color: var(--ink);
    text-transform: uppercase; text-align: center;
  }
  /* Back */
  .card--back {
    background: radial-gradient(circle at 40% 70%, var(--red) 0%, var(--red-deep) 100%);
  }
  .card--back .decor-circle {
    position: absolute; width: 360px; height: 360px; border-radius: 50%;
    left: -60px; top: 40px; background: var(--faint-red);
  }
  .card--back .name {
    position: absolute; right: 50px; top: 110px;
    font-weight: 900; font-size: 22px; line-height: 1.05; color: var(--gold);
    text-transform: uppercase; text-align: center;
  }
</style>
</head>
<body>
<main class="sheet">
  <section class="card card--front" aria-label="Business card front">
    <div class="decor-circle"></div>
    <div class="contact">
      <p class="person">Sensei Daniel R. Okoro</p>
      <p class="role">Instructor</p>
      <p class="studio">Lakemont Kenbu Kai<br>Karate Studio</p>
      <p class="address">Maplecrest Plaza<br>38214 US Hwy. 61<br>Harlow Springs, Ohio. 33812</p>
      <p><span class="label">p</span>407-555-0183</p>
      <p><span class="label">e</span>Lakemontkenbukaistudio@samplemail.net</p>
    </div>
    <div class="brand">
      <div class="mark-dot"></div>
      <p class="name">Lakemont<br>Kenbu Kai<br>Karate</p>
    </div>
  </section>
  <section class="card card--back" aria-label="Business card back">
    <div class="decor-circle"></div>
    <p class="name">Lakemont<br>Kenbu Kai<br>Karate</p>
  </section>
</main>
</body>
</html>
```